business card deign

Logo needs the following on it.
1. attached logo
2. Tagline - "From icy coolers to loud speakers...we bring the fun!"
3. Name- Dalia Fenwick, Founder and CPO
4. Address - 482 E. Calder Avenue, Ste 2207, Tampa, FL. 33719
5. Phone - 720.555.0183

```html
<!DOCTYPE html>
<html lang="en">
<head>
<meta charset="UTF-8">
<title>Hopwell Business Card</title>
<link rel="stylesheet" href="https://fonts.googleapis.com/css2?family=Montserrat:wght@400;500;700&display=swap">
<style>
  :root {
    --backdrop: #2e2e2e;
    --card-white: #ffffff;
    --ink: #0c0c0c;
    --ink-soft: #2a2a2a;
    --band: #050505;
    --band-text: #ffffff;
    --pattern-light: #6a6a6a;
    --pattern-dark: #0d0d0d;
  }
  * { box-sizing: border-box; margin: 0; padding: 0; }
  html, body {
    width: 1200px;
    height: 689px;
    overflow: hidden;
    background: var(--backdrop);
    font-family: "Montserrat", sans-serif;
  }
  .canvas {
    position: relative;
    width: 1200px;
    height: 689px;
  }
  .card {
    position: absolute;
    top: 195px;
    width: 520px;
    height: 300px;
    border-radius: 24px;
    overflow: hidden;
  }
  .card--back {
    left: 50px;
    background: var(--pattern-dark);
  }
  .card--back .brand-pattern {
    position: absolute;
    inset: 0;
    background: linear-gradient(35deg, var(--pattern-light) 0%, #333 30%, #161616 60%, var(--pattern-dark) 100%);
  }
  .card--front {
    left: 630px;
    background: var(--card-white);
    color: var(--ink);
  }
  .wordmark {
    position: absolute;
    top: 58px;
    left: 0;
    width: 100%;
    text-align: center;
    font-weight: 700;
    font-size: 40px;
    letter-spacing: 14px;
    padding-left: 14px;
    color: var(--ink);
  }
  .person {
    position: absolute;
    top: 150px;
    right: 284px;
    text-align: right;
  }
  .person__name {
    font-weight: 700;
    font-size: 22px;
    line-height: 1.1;
    white-space: nowrap;
  }
  .person__title {
    font-weight: 400;
    font-size: 15px;
    color: var(--ink-soft);
    margin-top: 3px;
  }
  .divider {
    position: absolute;
    left: 255px;
    top: 128px;
    width: 1.5px;
    height: 86px;
    background: var(--ink);
  }
  .contact {
    position: absolute;
    left: 274px;
    top: 134px;
    font-size: 13px;
    line-height: 1.45;
    color: var(--ink-soft);
  }
  .contact__phone {
    display: flex;
    align-items: center;
    gap: 6px;
    margin-bottom: 12px;
  }
  .contact__phone svg { width: 13px; height: 13px; }
  .tagline-band {
    position: absolute;
    left: 0;
    top: 234px;
    width: 100%;
    height: 30px;
    background: var(--band);
    color: var(--band-text);
    font-size: 13.5px;
    font-weight: 500;
    display: flex;
    align-items: center;
    justify-content: center;
    letter-spacing: 0.2px;
    white-space: nowrap;
  }
</style>
</head>
<body>
<main class="canvas">
  <section class="card card--back" aria-label="Card back">
    <div class="brand-pattern" role="img" aria-label="Repeating brand-mark pattern fading from grey to black"></div>
  </section>

  <section class="card card--front" aria-label="Card front">
    <div class="wordmark">HOPWELL</div>

    <div class="person">
      <p class="person__name">Dalia Fenwick</p>
      <p class="person__title">Founder and CPO</p>
    </div>

    <div class="divider"></div>

    <div class="contact">
      <p class="contact__phone">
        <svg viewBox="0 0 24 24" aria-hidden="true"><path fill="#111" d="M6.6 10.8a15.1 15.1 0 0 0 6.6 6.6l2.2-2.2a1 1 0 0 1 1-.25 11.4 11.4 0 0 0 3.6.57 1 1 0 0 1 1 1V20a1 1 0 0 1-1 1A17 17 0 0 1 3 4a1 1 0 0 1 1-1h3.5a1 1 0 0 1 1 1c0 1.25.2 2.45.57 3.57a1 1 0 0 1-.25 1z"/></svg>
        720.555.0183
      </p>
      <p class="contact__address">482 E. Calder Avenue, Ste<br>2207, Tampa, FL. 33719</p>
    </div>

    <div class="tagline-band">From icy coolers to loud speakers...we bring the fun!</div>
  </section>
</main>
</body>
</html>
```